business card design for a small scale specialty cut flower farm

We need a business card design for Hollowmere Bloom Farm based in Langley, BC, Canada. We produce specialty, high-end cut flowers and sell locally to florists, local shops and markets and the end user through bouquet subscriptions. The final business card design should be memorable and have a timeless or vintage feel. We would prefer a square shape.
Updates

Target Market(s)

florists, shops and seasonal markets, local flower lovers

Industry/Entity Type

Floral

Contact Information for Business Card

Tamsin Ellery Voss, Grower
Langley, BC, Canada
website: hollowmerebloomfarm.example
instagram: @hollowmerebloomfarm
Tel: 555.317.4290
facebook: www.facebook.example/hollowmereblooms/

Font styles to use
Serif
Decorative
Script

Requirements
Must have
• soft black background colour on front side, the included logo and catch phrase: Fresh Local Seasonal
Nice to have
• phone number and website address on front of card, included photo 6539 incorporated onto the back, possibly photo 6609 as well.

```html
<!DOCTYPE html>
<html lang="en">
<head>
<meta charset="utf-8">
<title>Hollowmere Bloom Farm – Business Card</title>
<link rel="stylesheet" href="https://fonts.googleapis.com/css2?family=Great+Vibes&family=Lora:ital,wght@0,400;0,700;1,400&display=swap">
<style>
  :root {
    --stage: #ece8e3;
    --soft-black: #141414;
    --soft-black-pattern: #1f1f1f;
    --frame-light: #8a8a8a;
    --card-white: #ffffff;
    --pattern-grey: #eeeeee;
    --frame-dark: #9a9a9a;
    --ink: #1c1c1c;
    --leaf-green: #5c8a4a;
    --petal-pink: #efb6cf;
    --rule: #555555;
  }
  * { margin: 0; padding: 0; box-sizing: border-box; }
  html, body { width: 1200px; height: 800px; overflow: hidden; }
  body {
    background: var(--stage);
    display: flex;
    align-items: center;
    justify-content: center;
    gap: 80px;
    font-family: "Lora", Georgia, serif;
  }
  .card {
    position: relative;
    width: 440px;
    height: 440px;
    border-radius: 30px;
    overflow: hidden;
    box-shadow: 0 8px 24px rgba(0,0,0,0.18);
  }
  .card-pattern {
    position: absolute;
    inset: 0;
  }
  .card-frame {
    position: absolute;
    inset: 16px;
    border-radius: 22px;
    border: 1px solid var(--frame-light);
  }

  /* Front */
  .card--front { background: var(--soft-black); }
  .card--front .card-pattern {
    background: radial-gradient(circle at 50% 50%, var(--soft-black-pattern), var(--soft-black) 75%);
  }
  .front-brand {
    position: absolute;
    left: 0; right: 0;
    top: 150px;
    display: flex;
    align-items: center;
    justify-content: center;
    gap: 16px;
  }
  .brand-mark {
    width: 58px; height: 58px;
    border-radius: 50%;
    background: var(--petal-pink);
    flex: none;
  }
  .brand-name {
    color: #ffffff;
    font-family: "Lora", Georgia, serif;
    font-weight: 400;
    font-size: 34px;
    line-height: 1.15;
    letter-spacing: 0.5px;
  }

  /* Back */
  .card--back { background: var(--card-white); }
  .card--back .card-pattern { background: var(--pattern-grey); opacity: 0.6; }
  .card--back .card-frame { border-color: var(--frame-dark); }
  .back-content {
    position: absolute;
    inset: 0;
    padding: 46px 58px 0;
    color: var(--ink);
  }
  .holder-name {
    text-align: center;
    font-weight: 700;
    font-size: 24px;
  }
  .holder-role {
    text-align: center;
    font-style: italic;
    color: var(--leaf-green);
    font-size: 17px;
    margin-top: 2px;
  }
  .divider {
    position: relative;
    height: 28px;
    margin: 6px 0 10px;
  }
  .divider::before {
    content: "";
    position: absolute;
    left: 0; right: 0; top: 50%;
    border-top: 1px solid var(--rule);
  }
  .divider-bloom {
    position: absolute;
    left: 50%; top: 50%;
    width: 26px; height: 26px;
    margin: -13px 0 0 -13px;
    border-radius: 50%;
    background: radial-gradient(circle, #e9e27a 25%, var(--petal-pink) 30%);
  }
  .contact-list { list-style: none; font-size: 17px; line-height: 1.6; }
  .contact-item { display: flex; align-items: center; gap: 10px; }
  .contact-icon { width: 18px; height: 18px; flex: none; }
  .contact-item--plain { padding-left: 28px; }
  .tagline {
    font-family: "Great Vibes", cursive;
    font-size: 34px;
    text-align: center;
    margin-top: 2px;
  }
</style>
</head>
<body>

  <section class="card card--front" aria-label="Card front">
    <div class="card-pattern" role="img" aria-label="Faint dark damask pattern"></div>
    <div class="card-frame"></div>
    <div class="front-brand">
      <span class="brand-mark"></span>
      <span class="brand-name">Hollowmere<br>Bloom Farm</span>
    </div>
  </section>

  <section class="card card--back" aria-label="Card back">
    <div class="card-pattern" role="img" aria-label="Soft grey damask pattern"></div>
    <div class="card-frame"></div>
    <div class="back-content">
      <p class="holder-name">Tamsin Ellery Voss</p>
      <p class="holder-role">Owner</p>
      <div class="divider"><span class="divider-bloom" role="img" aria-label="Small pink wild rose ornament"></span></div>
      <ul class="contact-list">
        <li class="contact-item">
          <svg class="contact-icon" viewBox="0 0 20 20" aria-hidden="true">
            <circle cx="10" cy="10" r="10" fill="#1c1c1c"/>
            <path d="M6.5 5.5l2 0 1 2.5-1.3 1a6 6 0 0 0 2.8 2.8l1-1.3 2.5 1v2a1 1 0 0 1-1 1A8 8 0 0 1 5.5 6.5a1 1 0 0 1 1-1z" fill="#fff"/>
          </svg>
          (555) 317-4290
        </li>
        <li class="contact-item">
          <svg class="contact-icon" viewBox="0 0 20 20" aria-hidden="true"><circle cx="10" cy="10" r="10" fill="#1c1c1c"/></svg>
          @hollowmerebloomfarm
        </li>
        <li class="contact-item contact-item--plain">hollowmerebloomfarm.example</li>
        <li class="contact-item">
          <svg class="contact-icon" viewBox="0 0 20 20" aria-hidden="true"><circle cx="10" cy="10" r="10" fill="#1c1c1c"/></svg>
          hollowmereblooms
        </li>
      </ul>
      <div class="divider"><span class="divider-bloom" role="img" aria-label="Small pink wild rose ornament"></span></div>
      <p class="tagline">Fresh Local Seasonal</p>
    </div>
  </section>

</body>
</html>
```